Velvet Dare Age Verification Landing Page

To create a visually appealing design for the landing page of the adult game "Velvet Dare" that confirms the visitor's age.
The design should have a simple and visually appealing look that focuses on two buttons labeled "Yes" and "No". The purpose of the page is to confirm that the visitor is 18 years of age or older before accessing the game's content. Responsive design that works well on desktop and mobile devices. The final output should be delivered in PSD, AI, or Sketch format, along with any necessary images or assets.
I have also attached examples.

```html
<!DOCTYPE html>
<html lang="en">
<head>
<meta charset="utf-8">
<title>Velvet Dare – Age Verification</title>
<link rel="stylesheet" href="https://fonts.googleapis.com/css2?family=Inter:wght@400;500;600;700&display=swap">
<style>
  :root {
    --ink: #201f20;
    --plum: #9a5d98;
    --orchid: #bc7cb9;
    --blush: #fff5f5;
    --board: #ebdfea;
    --muted: #6b6270;
    --rule: #cfc2cf;
    --night: #0b070b;
    --card: rgba(38, 34, 40, 0.82);
    --card-edge: rgba(255, 255, 255, 0.16);
  }
  * { box-sizing: border-box; margin: 0; padding: 0; }
  html, body { width: 978px; height: 1200px; overflow: hidden; }
  body {
    background: var(--board);
    font-family: "Inter", Arial, sans-serif;
    color: var(--ink);
    position: relative;
  }

  /* ---------- brand sheet header ---------- */
  .brand-sheet { position: absolute; left: 0; top: 0; width: 978px; height: 180px; }
  .sheet-logo {
    position: absolute; left: 137px; top: 104px;
    display: flex; align-items: center; gap: 8px;
    font-weight: 600; font-size: 20px; color: var(--plum);
  }
  .sheet-logo .mark-dot { width: 14px; height: 14px; border-radius: 50%; background: var(--plum); }
  .divider { position: absolute; top: 84px; width: 1px; height: 81px; background: var(--rule); }
  .divider.first { left: 353px; }
  .divider.second { left: 618px; }
  .spec-title { position: absolute; top: 84px; font-size: 20px; font-weight: 400; color: var(--ink); }
  .fonts-title { left: 457px; }
  .font-name { position: absolute; left: 457px; top: 124px; font-size: 13px; color: var(--muted); }
  .colors-title { left: 722px; }
  .swatches { position: absolute; left: 722px; top: 116px; display: flex; gap: 9px; }
  .swatch { width: 35px; display: flex; flex-direction: column; align-items: center; gap: 6px; }
  .swatch .chip { width: 34px; height: 34px; border-radius: 50%; box-shadow: 0 1px 3px rgba(0,0,0,.12); }
  .swatch .hex { font-size: 8px; color: var(--muted); white-space: nowrap; }

  /* ---------- screens ---------- */
  .screen {
    position: absolute; overflow: hidden;
    background: var(--night);
    display: flex; align-items: center; justify-content: center;
  }
  .hero-photo {
    position: absolute; inset: 0;
    background:
      linear-gradient(90deg, transparent 46%, rgba(154,93,152,.28) 48%, rgba(154,93,152,.28) 50%, transparent 52%),
      radial-gradient(ellipse 38% 22% at 62% 36%, rgba(154,93,152,.38), transparent 70%),
      radial-gradient(ellipse 30% 34% at 32% 52%, rgba(120,70,120,.35), transparent 70%),
      radial-gradient(ellipse 70% 60% at 50% 50%, rgba(60,30,60,.5), transparent 80%),
      var(--night);
  }
  .laptop-screen { left: 154px; top: 237px; width: 645px; height: 403px; font-size: 8.1px; box-shadow: 0 20px 40px rgba(60,30,60,.25); }
  .phone-screen { left: 737px; top: 480px; width: 114px; height: 244px; font-size: 4.12px; border-radius: 10px; box-shadow: 0 14px 30px rgba(40,20,40,.35); }
  .desktop-screen { left: 82px; top: 766px; width: 616px; height: 343px; font-size: 6.86px; }
  .mobile-screen { left: 707px; top: 766px; width: 180px; height: 343px; font-size: 6.86px; }

  /* ---------- age gate dialog ---------- */
  .age-gate {
    position: relative; z-index: 1;
    width: 33em;
    padding: 3.2em 2em 2.8em;
    background: var(--card);
    border: 0.1em solid var(--card-edge);
    border-radius: 0.8em;
    box-shadow: 0 0 0 0.5em rgba(20,18,22,.45);
    text-align: center; color: #fff;
  }
  .age-gate.compact { width: 22.8em; padding: 3.6em 1.4em 3em; }
  .gate-logo {
    display: flex; align-items: center; justify-content: center; gap: 0.7em;
    height: 7em;
    font-weight: 600; font-size: 1em; color: var(--orchid);
  }
  .gate-logo .name { font-size: 2.6em; }
  .gate-logo .mark-dot { width: 2em; height: 2em; border-radius: 50%; background: var(--blush); }
  .gate-title { margin-top: 3em; font-size: 2.2em; line-height: 1.2; font-weight: 700; }
  .compact .gate-title { margin-top: 2em; font-size: 1.9em; }
  .gate-text { margin-top: 1.5em; font-size: 1em; line-height: 1.55; color: #d9d2da; font-weight: 400; }
  .compact .gate-text { font-size: 1.05em; }
  .gate-actions { margin-top: 1.8em; display: flex; justify-content: center; gap: 0.6em; }
  .btn {
    width: 9.6em; height: 3.3em; border-radius: 1.65em;
    display: flex; align-items: center; justify-content: center;
    font-size: 0.9em; font-weight: 600; text-transform: uppercase; letter-spacing: 0.02em;
  }
  .btn span { font-size: 0.9em; }
  .btn-yes { background: linear-gradient(90deg, var(--plum), var(--orchid)); color: #fff; }
  .btn-no { background: var(--blush); color: var(--plum); }
  .remember { margin-top: 1.7em; display: flex; justify-content: center; align-items: center; gap: 0.6em; font-size: 0.85em; color: #d9d2da; }
  .remember svg { width: 1.1em; height: 1.1em; }
</style>
</head>
<body>

<header class="brand-sheet">
  <div class="sheet-logo"><span class="mark-dot"></span>Velvet Dare</div>
  <div class="divider first"></div>
  <div class="spec-title fonts-title">Fonts:</div>
  <div class="font-name">Inter</div>
  <div class="divider second"></div>
  <div class="spec-title colors-title">Colors:</div>
  <div class="swatches">
    <div class="swatch"><div class="chip" style="background: var(--ink)"></div><div class="hex">#201f20</div></div>
    <div class="swatch"><div class="chip" style="background: var(--plum)"></div><div class="hex">#9a5d98</div></div>
    <div class="swatch"><div class="chip" style="background: var(--orchid)"></div><div class="hex">#bc7cb9</div></div>
    <div class="swatch"><div class="chip" style="background: var(--blush)"></div><div class="hex">#fff5f5</div></div>
  </div>
</header>

<!-- desktop preview -->
<section class="screen laptop-screen">
  <div class="hero-photo" role="img" aria-label="Blurred purple-toned photo of a pole dancer behind the dialog"></div>
  <div class="age-gate">
    <div class="gate-logo"><span class="mark-dot"></span><span class="name">Velvet Dare</span></div>
    <h1 class="gate-title">The site contains sexually<br>explicit material</h1>
    <p class="gate-text">You are going to see a lot of strip variations at home.<br>Are you over 18 years of age?</p>
    <div class="gate-actions">
      <div class="btn btn-yes"><span>Yes, I am</span></div>
      <div class="btn btn-no"><span>No, I am not</span></div>
    </div>
    <div class="remember">
      <svg viewBox="0 0 12 12"><rect x="0.5" y="0.5" width="11" height="11" rx="1.5" fill="none" stroke="#8d8590"/><path d="M3 6.2l2 2 4-4.4" fill="none" stroke="#d9d2da" stroke-width="1.2"/></svg>
      Remember Me
    </div>
  </div>
</section>

<!-- mobile preview -->
<section class="screen phone-screen">
  <div class="hero-photo" role="img" aria-label="Blurred purple-toned photo of a pole dancer behind the dialog"></div>
  <div class="age-gate compact">
    <div class="gate-logo"><span class="mark-dot"></span><span class="name">Velvet Dare</span></div>
    <h1 class="gate-title">The site<br>contains sexually<br>explicit material</h1>
    <p class="gate-text">You are going to see a lot of<br>strip variations at home.<br>Are you over 18 years of age?</p>
    <div class="gate-actions">
      <div class="btn btn-yes"><span>Yes, I am</span></div>
      <div class="btn btn-no"><span>No, I am not</span></div>
    </div>
    <div class="remember">
      <svg viewBox="0 0 12 12"><rect x="0.5" y="0.5" width="11" height="11" rx="1.5" fill="none" stroke="#8d8590"/><path d="M3 6.2l2 2 4-4.4" fill="none" stroke="#d9d2da" stroke-width="1.2"/></svg>
      Remember Me
    </div>
  </div>
</section>

<!-- desktop layout -->
<section class="screen desktop-screen">
  <div class="hero-photo" role="img" aria-label="Blurred purple-toned photo of a pole dancer behind the dialog"></div>
  <div class="age-gate">
    <div class="gate-logo"><span class="mark-dot"></span><span class="name">Velvet Dare</span></div>
    <h1 class="gate-title">The site contains sexually<br>explicit material</h1>
    <p class="gate-text">You are going to see a lot of strip variations at home.<br>Are you over 18 years of age?</p>
    <div class="gate-actions">
      <div class="btn btn-yes"><span>Yes, I am</span></div>
      <div class="btn btn-no"><span>No, I am not</span></div>
    </div>
    <div class="remember">
      <svg viewBox="0 0 12 12"><rect x="0.5" y="0.5" width="11" height="11" rx="1.5" fill="none" stroke="#8d8590"/><path d="M3 6.2l2 2 4-4.4" fill="none" stroke="#d9d2da" stroke-width="1.2"/></svg>
      Remember Me
    </div>
  </div>
</section>

<!-- mobile layout -->
<section class="screen mobile-screen">
  <div class="hero-photo" role="img" aria-label="Blurred purple-toned photo of a pole dancer behind the dialog"></div>
  <div class="age-gate compact">
    <div class="gate-logo"><span class="mark-dot"></span><span class="name">Velvet Dare</span></div>
    <h1 class="gate-title">The site<br>contains sexually<br>explicit material</h1>
    <p class="gate-text">You are going to see a lot of<br>strip variations at home.<br>Are you over 18 years of age?</p>
    <div class="gate-actions">
      <div class="btn btn-yes"><span>Yes, I am</span></div>
      <div class="btn btn-no"><span>No, I am not</span></div>
    </div>
    <div class="remember">
      <svg viewBox="0 0 12 12"><rect x="0.5" y="0.5" width="11" height="11" rx="1.5" fill="none" stroke="#8d8590"/><path d="M3 6.2l2 2 4-4.4" fill="none" stroke="#d9d2da" stroke-width="1.2"/></svg>
      Remember Me
    </div>
  </div>
</section>

</body>
</html>
```